Harbor's Lantern Beer Label Design

Brass Dory Beer Co. wants to create a 12oz beer can label for its newest release of a Grapefruit Session IPA called Harbor's Lantern. Brass Dory is currently only sold on draft in the state of South Carolina, USA and is considered "coastal craft beer" with most of our beer styles having lower alcohol content so they can be enjoyed in the heat of the outdoors, on the beach, boating, etc.

Story behind the name: A "Harbor’s Brass Lantern" is a carved wooden figurehead of a woman on a ship’s bow. Figureheads embodied the spirit of a ship and were believed to placate the gods of the sea to ensure a safe voyage. This should be the premise of the can design...most female figureheads on ships in the 18th and 19th century had large breasts, many times exposed, but this is not necessarily what we are looking for as we do NOT want to demean females in any way but would rather put them on a pedestal due to the power a female figurehead held (calming the sea god, Neptune, so he would ensure the ship had safe passage)

The attached eps file is to be used as the template. The label will be printed and attached to a stock can during the filling process. Please be aware that the stock can is black and the can will show black above and below the label once applied. The only graphics, from the attached template, that should remain on this can label are the UPC code (FPO), the Surgeon General warning and the verbiage in the bottom black section that states 12 fl oz 355 ml, Alc/Vol, etc. The ABV for this beer should be listed as 4.9% Alc./Vol. and "brewed by" should read: Brewed and Canned for Brass Dory Beer Co.
by Carrow Brewing Co.; Lancaster, South Carolina

There will need to be a prominent spots for both the Brass Dory logo (attached) and the beer style (Session Grapefruit IPA). We will also be including a "story" which will need a column carved out to contain approx. 36-40 words (you do not need to create the story, just the illustration)

The demographic for craft beer is primarily male but females enjoy our beer as well. A creative, bold and fun design is what we are looking for instead of plain and corporate looking. Keep in mind the design will be next to hundreds of other designs on store shelves so it needs to attract the consumer's eye.

Please ask any questions that may help you create an award winning design!

Target Market(s)

Craft Beer drinkers, ages 21-45

Colors

Designer to choose colors to be used in the design.

Requirements
Must have
• Brass Dory logo
• Incorporate beer style: Grapefruit Session IPA
• Text in black area at bottom of template
• Area for 36-40 word "story"
Nice to have
• stormy sea and calm sea
• A female wooden figurehead on a ship's bow
• Neptune
• Trident
Should not have
• Nudity
• any graphic that would offend females
• any graphic that would be rejected by the Beverage and Label Office who will approve the label design (BLRA)

```html
<!DOCTYPE html>
<html lang="en">
<head>
<meta charset="utf-8">
<title>Brass Dory – Grapefruit Session IPA Label</title>
<link rel="stylesheet" href="https://fonts.googleapis.com/css2?family=Cinzel:wght@400;700;900&display=swap">
<style>
  :root {
    --backdrop: #eeeeee;
    --storm-light: #f4f4f4;
    --storm-mid: #d6d6d6;
    --storm-dark: #a9a9a9;
    --band-black: #0b0b0c;
    --accent-blue: #2a9bd6;
    --sea-deep: #050f16;
    --sea-mid: #0f3447;
    --sea-light: #2a6a80;
    --ink: #111111;
    --fine-print: #c9d3d8;
  }
  html, body {
    margin: 0;
    padding: 0;
    width: 1200px;
    height: 1200px;
    overflow: hidden;
    background: var(--backdrop);
  }
  .canvas {
    width: 1200px;
    height: 1200px;
    display: flex;
    align-items: center;
    justify-content: center;
  }
  .label {
    display: block;
    width: 560px;
    height: 1000px;
    box-shadow: 0 18px 40px rgba(0,0,0,0.18);
  }
  .brand-name {
    font-family: "Cinzel", serif;
    font-weight: 900;
    fill: var(--ink);
    letter-spacing: 6px;
  }
  .style-name {
    font-family: "Cinzel", serif;
    font-weight: 400;
    fill: var(--accent-blue);
    letter-spacing: 1px;
  }
  .abv {
    font-family: "Cinzel", serif;
    font-weight: 400;
    fill: var(--fine-print);
    letter-spacing: 1px;
  }
  .story {
    font-family: "Cinzel", serif;
    font-weight: 400;
    font-size: 10px;
    fill: var(--fine-print);
  }
  .volume-line {
    font-family: "Cinzel", serif;
    font-weight: 700;
    font-size: 14px;
    fill: var(--fine-print);
    letter-spacing: 1px;
  }
  .brewed-by {
    font-family: "Cinzel", serif;
    font-weight: 400;
    font-size: 8.5px;
    fill: var(--fine-print);
  }
  .warning {
    font-family: "Cinzel", serif;
    font-weight: 400;
    font-size: 6.5px;
    fill: var(--fine-print);
  }
</style>
</head>
<body>
<main class="canvas">
  <svg class="label" viewBox="0 0 560 1000" xmlns="http://www.w3.org/2000/svg">
    <defs>
      <linearGradient id="storm-sky" x1="0" y1="0" x2="0" y2="1">
        <stop offset="0" stop-color="var(--storm-dark)"/>
        <stop offset="0.3" stop-color="var(--storm-light)"/>
        <stop offset="0.7" stop-color="var(--storm-mid)"/>
        <stop offset="1" stop-color="var(--storm-light)"/>
      </linearGradient>
      <radialGradient id="stormy-sea" cx="0.35" cy="0.55" r="0.8">
        <stop offset="0" stop-color="var(--sea-light)"/>
        <stop offset="0.45" stop-color="var(--sea-mid)"/>
        <stop offset="1" stop-color="var(--sea-deep)"/>
      </radialGradient>
    </defs>

    <!-- stormy sea -->
    <rect class="sea-scene" x="0" y="0" width="560" height="1000" fill="url(#stormy-sea)"
          role="img" aria-label="Dark stormy sea with a small wooden rowboat tossed by waves"/>

    <!-- lightning sky, cut into a V -->
    <polygon class="sky-scene" points="0,0 560,0 560,427 280,711 0,427" fill="url(#storm-sky)"
             role="img" aria-label="Grey storm sky lit by branching lightning"/>

    <!-- chevron band -->
    <polygon class="chevron-band" points="0,427 280,711 560,427 560,537 280,822 0,537" fill="var(--band-black)"/>
    <polyline class="chevron-rule" points="0,437 280,721 560,437" fill="none" stroke="var(--accent-blue)" stroke-width="3"/>
    <polyline class="chevron-rule" points="0,527 280,812 560,527" fill="none" stroke="var(--accent-blue)" stroke-width="3"/>

    <!-- brand name -->
    <text class="brand-name" x="280" y="285" font-size="84" text-anchor="middle">BRASS</text>
    <text class="brand-name" x="280" y="380" font-size="84" text-anchor="middle">DORY</text>

    <!-- beer style along the chevron -->
    <text class="style-name" x="142" y="626" font-size="44" text-anchor="middle" dominant-baseline="middle"
          transform="rotate(45.4 142 626)">GRAPEFRUIT</text>
    <text class="style-name" x="418" y="626" font-size="44" text-anchor="middle" dominant-baseline="middle"
          transform="rotate(-45.4 418 626)">SESSION IPA</text>

    <!-- strength -->
    <text class="abv" x="440" y="735" font-size="17" text-anchor="middle" dominant-baseline="middle"
          transform="rotate(-45.4 440 735)">4.9% ALC BY VOL</text>

    <!-- story column -->
    <g class="story-column">
      <text class="story" x="26" y="782">Sailors once trusted a</text>
      <text class="story" x="26" y="795">carved lantern on the bow</text>
      <text class="story" x="26" y="808">to calm the sea god and</text>
      <text class="story" x="26" y="821">guide them home. We brew</text>
      <text class="story" x="26" y="834">this bright grapefruit</text>
      <text class="story" x="26" y="847">session IPA in that spirit,</text>
      <text class="story" x="26" y="860">for sunny decks, long</text>
      <text class="story" x="26" y="873">beach days and safe</text>
      <text class="story" x="26" y="886">passage back to harbor.</text>
    </g>

    <!-- bottom black section -->
    <rect class="base-band" x="0" y="900" width="560" height="100" fill="var(--band-black)"/>
    <line class="base-rule" x1="0" y1="900" x2="560" y2="900" stroke="var(--accent-blue)" stroke-width="3"/>
    <text class="volume-line" x="280" y="922" text-anchor="middle">12 FL OZ · 355 ML · 4.9% ALC./VOL.</text>
    <text class="brewed-by" x="280" y="938" text-anchor="middle">Brewed and Canned for Brass Dory Beer Co.</text>
    <text class="brewed-by" x="280" y="950" text-anchor="middle">by Carrow Brewing Co.; Lancaster, South Carolina</text>
    <text class="warning" x="280" y="965" text-anchor="middle">GOVERNMENT WARNING: (1) ACCORDING TO THE SURGEON GENERAL, WOMEN SHOULD NOT</text>
    <text class="warning" x="280" y="973" text-anchor="middle">DRINK ALCOHOLIC BEVERAGES DURING PREGNANCY BECAUSE OF THE RISK OF BIRTH</text>
    <text class="warning" x="280" y="981" text-anchor="middle">DEFECTS. (2) CONSUMPTION OF ALCOHOLIC BEVERAGES IMPAIRS YOUR ABILITY TO</text>
    <text class="warning" x="280" y="989" text-anchor="middle">DRIVE A CAR OR OPERATE MACHINERY, AND MAY CAUSE HEALTH PROBLEMS.</text>
  </svg>
</main>
</body>
</html>
```